Business Card Design Project

Front back design preferred. Vertical card, not horizontal. Logo being developed by your group.

Industry/Entity Type

Business

Font styles to use
Serif

Colors

Designer to choose colors to be used in the design.

Requirements
Must have
• Logo being developed by your designers. Normal names, titles, www address, phone numbers, email, offices.
Should not have
• Fax number!

```html
<!DOCTYPE html>
<html lang="en">
<head>
<meta charset="utf-8">
<title>Solvane — Business Card, Front and Back</title>
<link rel="stylesheet" href="https://fonts.googleapis.com/css2?family=Source+Serif+4:wght@400;600;700&display=swap">
<style>
  :root {
    --backdrop: #ecebe8;
    --card: #ffffff;
    --ink: #3a3a3a;
    --ink-soft: #8a8a8a;
    --accent: #ea7a1c;
    --band-dark: #4a4a4c;
    --watermark: #f6f4f1;
  }
  * { box-sizing: border-box; margin: 0; padding: 0; }
  html, body {
    width: 1200px; height: 900px; overflow: hidden;
    background: var(--backdrop);
    font-family: "Source Serif 4", Georgia, serif;
    color: var(--ink);
  }
  .sheet {
    position: relative; width: 1200px; height: 900px;
    display: flex; justify-content: center; align-items: center; gap: 120px;
  }
  .card {
    position: relative; width: 340px; height: 590px;
    background: var(--card);
    box-shadow: 0 6px 18px rgba(0,0,0,0.14);
    overflow: hidden;
    display: flex; flex-direction: column; align-items: center;
  }
  .card__watermark {
    position: absolute; width: 300px; height: 300px; border-radius: 50%;
    background: var(--watermark); left: 110px; top: 320px;
  }
  .brand { position: relative; display: flex; flex-direction: column; align-items: center; }
  .brand__dot {
    width: 64px; height: 64px; border-radius: 50%; background: var(--accent);
    margin-bottom: 12px;
  }
  .brand__name {
    font-weight: 700; font-size: 50px; line-height: 1;
    color: var(--accent);
  }
  .brand__slogan { font-size: 10px; color: var(--ink-soft); margin-top: 6px; letter-spacing: 0.3px; }

  .card--front .brand { margin-top: 160px; }
  .card--front .website {
    position: absolute; bottom: 92px; width: 100%; text-align: center;
    font-size: 20px; color: var(--ink);
  }

  .card--back .band-top { width: 100%; height: 14px; background: var(--band-dark); }
  .card--back .band-bottom { position: absolute; bottom: 0; width: 100%; height: 14px; background: var(--accent); }
  .card--back .brand { margin-top: 36px; }
  .person { position: relative; margin-top: 18px; text-align: center; }
  .person__name { font-size: 22px; font-weight: 600; color: var(--ink); line-height: 1.2; }
  .person__title { font-size: 13px; color: var(--ink-soft); letter-spacing: 1px; text-transform: uppercase; margin-top: 2px; }
  .contacts { position: relative; list-style: none; margin-top: 16px; text-align: center; }
  .contact { display: flex; flex-direction: column; align-items: center; margin-bottom: 9px; }
  .contact__icon {
    width: 24px; height: 24px; border-radius: 50%; background: var(--accent);
    display: flex; align-items: center; justify-content: center; margin-bottom: 4px;
  }
  .contact__text { font-size: 17px; line-height: 1.3; color: var(--ink); }
</style>
</head>
<body>
<main class="sheet">

  <section class="card card--front" aria-label="Card front">
    <div class="card__watermark"></div>
    <div class="brand">
      <div class="brand__dot"></div>
      <div class="brand__name">Solvane</div>
      <div class="brand__slogan">Your slogan is here</div>
    </div>
    <p class="website">www.yourwebsite.com</p>
  </section>

  <section class="card card--back" aria-label="Card back">
    <div class="band-top"></div>
    <div class="card__watermark"></div>
    <div class="brand">
      <div class="brand__dot"></div>
      <div class="brand__name">Solvane</div>
      <div class="brand__slogan">Your slogan is here</div>
    </div>
    <div class="person">
      <p class="person__name">Your Name</p>
      <p class="person__title">Your Job Title</p>
    </div>
    <ul class="contacts">
      <li class="contact">
        <span class="contact__icon">
          <svg width="14" height="14" viewBox="0 0 14 14"><path d="M7 1a4 4 0 0 0-4 4c0 3 4 8 4 8s4-5 4-8a4 4 0 0 0-4-4z" fill="#fff"/><circle cx="7" cy="5" r="1.5" fill="#ea7a1c"/></svg>
        </span>
        <span class="contact__text">Your Commercial or office address</span>
      </li>
      <li class="contact">
        <span class="contact__icon">
          <svg width="14" height="14" viewBox="0 0 14 14"><path d="M3 2h2.5l1 3-1.5 1a7 7 0 0 0 3 3l1-1.5 3 1V11a1 1 0 0 1-1 1A9 9 0 0 1 2 3a1 1 0 0 1 1-1z" fill="#fff"/></svg>
        </span>
        <span class="contact__text">00.00.00.0000</span>
      </li>
      <li class="contact">
        <span class="contact__icon">
          <svg width="14" height="14" viewBox="0 0 14 14"><rect x="2" y="3.5" width="10" height="7" fill="#fff"/><path d="M2 3.5l5 4 5-4" stroke="#ea7a1c" stroke-width="1" fill="none"/></svg>
        </span>
        <span class="contact__text">yourname@yourwebsite.com</span>
      </li>
      <li class="contact">
        <span class="contact__icon">
          <svg width="14" height="14" viewBox="0 0 14 14" fill="none" stroke="#fff" stroke-width="1.2"><circle cx="7" cy="7" r="5"/><ellipse cx="7" cy="7" rx="2.2" ry="5"/><path d="M2 7h10"/></svg>
        </span>
        <span class="contact__text">www.yourwebsite.com</span>
      </li>
    </ul>
    <div class="band-bottom"></div>
  </section>

</main>
</body>
</html>
```